Logo + Business Card design for a new start-up

For a new start-up company, a global brand expansion agency (marketing, brand consulting solutions) we're looking for a creative designer to help us design both the company logo and business card for project managers.

The name of the company is 'Harrow Mark Partners' (abbreviated: HMP, website: harrowmarkpartners.example)

The logo design should give the company an image of "corporate" (serious), but not too plain/simple. Playing with overlapping fonts, or font colors is an option. Logo with only the abbreviation HMP is also an option.

The business cards need to have a touch of creativity to them, any style/colors can be used, and should underline the nature of business.

Industry/Entity Type

Business

```html
<!DOCTYPE html>
<html lang="en">
<head>
<meta charset="utf-8">
<title>Harrow Mark Partners — Business Card</title>
<link rel="stylesheet" href="https://fonts.googleapis.com/css2?family=Open+Sans:wght@400;600;700&display=swap">
<style>
  :root {
    --backdrop: #4a423c;
    --card: #0c0c0d;
    --card-edge: #000;
    --brand-blue: #1a86c8;
    --silver: #c9c9cb;
    --text-light: #d6d6d6;
    --text-muted: #b4b4b4;
  }
  * { margin: 0; padding: 0; box-sizing: border-box; }
  html, body {
    width: 1200px; height: 900px; overflow: hidden;
    background: var(--backdrop);
    font-family: "Open Sans", Arial, sans-serif;
  }
  .stage {
    position: relative; width: 1200px; height: 900px;
    display: flex; align-items: center; justify-content: center; gap: 60px;
  }
  .card {
    position: relative; width: 520px; height: 300px;
    background: var(--card);
    box-shadow: 0 14px 30px rgba(0,0,0,.55);
  }
  /* Front */
  .card-front .wordmark {
    position: absolute; left: 70px; top: 118px;
    font-size: 64px; font-weight: 700; color: var(--brand-blue);
    letter-spacing: 1px; line-height: 1;
  }
  .card-front .divider {
    position: absolute; left: 262px; top: 70px; width: 1px; height: 160px;
    background: linear-gradient(to bottom, transparent, var(--brand-blue) 45%, var(--brand-blue) 75%, transparent);
  }
  .contact {
    position: absolute; left: 284px; top: 66px; color: var(--text-light);
  }
  .contact .person-name {
    font-size: 17px; font-weight: 600; color: var(--brand-blue); line-height: 1.1;
  }
  .contact .person-role {
    font-size: 12px; color: var(--text-muted); margin-bottom: 14px;
  }
  .contact ul { list-style: none; }
  .contact li {
    display: flex; align-items: center; gap: 8px;
    font-size: 12px; line-height: 19px;
  }
  .contact li svg { width: 10px; height: 10px; fill: var(--brand-blue); flex: none; }
  .contact .address {
    margin-top: 20px; font-size: 12.5px; line-height: 18px; color: var(--text-light);
  }
  /* Back */
  .card-back .lockup {
    position: absolute; left: 0; right: 0; top: 0; bottom: 0;
    display: flex; align-items: center; justify-content: center; gap: 14px;
  }
  .card-back .lockup-square {
    width: 14px; height: 14px; background: var(--silver);
  }
  .card-back .company-name {
    font-size: 30px; font-weight: 600; color: var(--silver);
    letter-spacing: 1.5px; text-transform: uppercase;
  }
</style>
</head>
<body>
<main class="stage">
  <section class="card card-front" aria-label="Business card, front">
    <div class="wordmark">HMP</div>
    <div class="divider"></div>
    <div class="contact">
      <p class="person-name">Marek Wolanski</p>
      <p class="person-role">Managing Director</p>
      <ul>
        <li>
          <svg viewBox="0 0 10 10" aria-hidden="true"><path d="M2 0.5 L3.6 2.6 L2.7 3.6 Q3.8 5.9 6.3 7.2 L7.4 6.3 L9.5 7.9 L8.4 9.5 Q3.8 9.2 0.5 1.8 Z"/></svg>
          +44 20 7946 0321
        </li>
        <li>
          <svg viewBox="0 0 10 10" aria-hidden="true"><path d="M0 2 H10 V8.5 H0 Z M0.8 2.6 L5 5.6 L9.2 2.6" stroke="#0c0c0d" stroke-width="0.8"/></svg>
          mw@harrowmarkpartners.example
        </li>
        <li>
          <svg viewBox="0 0 10 10" aria-hidden="true"><path d="M4 6 L6 4" stroke="#1a86c8" stroke-width="1.4"/><rect x="0.5" y="5" width="4.5" height="3" rx="1.5" transform="rotate(-45 2.75 6.5)" fill="none" stroke="#1a86c8" stroke-width="1.2"/><rect x="5" y="2" width="4.5" height="3" rx="1.5" transform="rotate(-45 7.25 3.5)" fill="none" stroke="#1a86c8" stroke-width="1.2"/></svg>
          www.harrowmarkpartners.example
        </li>
      </ul>
      <p class="address">12 Fenwick Row,<br>London EC9 4QT, UK</p>
    </div>
  </section>

  <section class="card card-back" aria-label="Business card, back">
    <div class="lockup">
      <span class="lockup-square"></span>
      <span class="company-name">Harrow Mark Partners</span>
    </div>
  </section>
</main>
</body>
</html>
```